Innovation and Optimisation Consultancy business needs a Wix website design

The task details are in the attached project brief. The attached pdf should give you a good outline of what is required. Colour guidance and look and feel guidelines are in the pdf file. The company is based in S.E.Asia.

Can be done as design files, but prefer it to be designed direct in WIX.

If you have any questions just ask.

I really don't know what will attract clients to my website so am leaving it to you to do something inspiring and innovative.

Target Market(s)

Organisations that don't just want to compete in their market, but that want to be number one in their market and be sure they stay there.

Industry/Entity Type

All

Requirements
Must have
• I don't know, I specialise in optimising businesses and inventing new products.
Nice to have
• Surprise me.

```html
<!DOCTYPE html>
<html lang="en">
<head>
<meta charset="utf-8">
<title>Novara Consult</title>
<link href="https://fonts.googleapis.com/css2?family=Poppins:wght@400;500;600;700;800&family=Montserrat:ital,wght@0,400;0,500;0,600;1,400;1,500&display=swap" rel="stylesheet">
<style>
:root{
  --maroon:#5b1628;
  --maroon-dark:#3f0d1b;
  --ink:#1f1b1e;
  --muted:#6f6266;
  --green:#4ec97b;
  --green-soft:#a9d9a5;
  --peach:#efd6c7;
  --peach-deep:#e6bfa9;
  --cream:#f8f1ee;
  --navy:#17203d;
  --line:#dcd2cf;
  --white:#ffffff;
}
*{box-sizing:border-box;margin:0;padding:0}
html,body{width:1200px;height:4383px;overflow:hidden}
body{position:relative;background:var(--white);font-family:"Montserrat",sans-serif;color:var(--ink)}
.abs{position:absolute}
.heading-font{font-family:"Poppins",sans-serif}

/* hero */
.hero{left:0;top:0;width:1200px;height:715px;background:linear-gradient(90deg,#efd3c2 0%,#f5e3d8 40%,#e9d6cf 62%,#c9c9cf 100%)}
.hero-photo{left:640px;top:0;width:560px;height:715px;background:radial-gradient(ellipse at 55% 45%,#3b4656 0%,#56606d 35%,#a9a7ad 70%,rgba(233,214,205,0) 100%)}
.nav-logo{left:131px;top:28px;font-family:"Poppins",sans-serif;font-size:31px;color:var(--maroon);font-weight:500}
.nav-links{left:428px;top:36px;display:flex;gap:62px;font-family:"Poppins",sans-serif;font-size:17px;color:var(--ink)}
.nav-links .active{border-bottom:2px solid var(--maroon);padding-bottom:6px}
.nav-cta{left:964px;top:29px;width:143px;height:40px;border-radius:20px;background:var(--green);color:#fff;font-family:"Poppins",sans-serif;font-size:13px;display:flex;align-items:center;justify-content:center}
.hero-kicker{left:124px;top:222px;font-size:19px;color:#3a2a2e;display:flex;align-items:center;gap:10px}
.hero-kicker::after{content:"";display:block;width:82px;height:1.5px;background:#3a2a2e}
.hero-title{left:124px;top:250px;font-family:"Poppins",sans-serif;font-size:52px;line-height:58px;color:var(--maroon-dark)}
.hero-title b{font-weight:800}
.hero-title span{font-weight:400;color:#2a1f22}
.hero-text{left:124px;top:378px;width:400px;font-size:15px;line-height:24px;color:#3d3336}
.hero-btn{left:126px;top:446px;width:168px;height:46px;border-radius:23px;background:var(--maroon);color:#fff;font-family:"Poppins",sans-serif;font-size:15px;display:flex;align-items:center;justify-content:center}
.scroll-badge{left:124px;top:553px}

/* section titles */
.sec-title{left:0;width:1200px;text-align:center;font-family:"Poppins",sans-serif;font-size:40px;font-weight:700;color:var(--ink)}
.sec-title::after{content:"";display:block;margin:10px auto 0;width:44px;height:3px;background:#5c6878}

/* problems */
.problems{left:0;top:715px;width:1200px;height:681px;background:#fff}
.photo-circle{border-radius:50%;border:4px solid #e4e0e0;box-shadow:0 0 0 10px rgba(255,255,255,.9),0 12px 30px rgba(0,0,0,.08)}
.prob-card{left:677px;width:392px;height:109px;border:1.5px solid #e2c6cd;border-radius:55px;background:#fff;box-shadow:0 6px 16px rgba(91,22,40,.06)}
.prob-card .icon{position:absolute;left:14px;top:12px;width:85px;height:85px;border-radius:50%;background:var(--maroon);display:flex;align-items:center;justify-content:center}
.card-h{font-family:"Poppins",sans-serif;font-size:18px;font-weight:600;color:var(--ink)}
.card-p{font-size:11.5px;line-height:17px;color:#4b4245;margin-top:6px}
.prob-card .txt{position:absolute;left:120px;top:26px;width:250px}

/* solutions */
.solutions{left:5px;top:1396px;width:1195px;height:677px;background:var(--cream)}
.sol-card{left:82px;width:389px;height:109px;border:1.5px solid #bfe2c4;border-radius:55px;background:#fff;box-shadow:0 6px 16px rgba(60,140,80,.06)}
.sol-card .txt{position:absolute;left:48px;top:26px;width:230px}
.sol-card .icon{position:absolute;right:12px;top:12px;width:85px;height:85px;border-radius:50%;background:var(--green);display:flex;align-items:center;justify-content:center}

/* benefits */
.benefits{left:0;top:2073px;width:1200px;height:957px;background:linear-gradient(180deg,#f0d9cb 0%,#eed2c2 55%,#f4e2d7 100%)}
.benefit-title{left:0;width:1200px;top:2125px;text-align:center;font-family:"Poppins",sans-serif;font-size:42px;color:var(--navy)}
.benefit-title b{font-weight:700}
.benefit-title::after{content:"";display:block;margin:8px auto 0;width:44px;height:3px;background:#5c6878}
.diamond{width:242px;height:242px;background:#fff;transform:rotate(45deg);box-shadow:0 8px 20px rgba(120,60,40,.06)}
.benefit-body{width:240px;text-align:center}
.benefit-body .icon{height:56px;display:flex;justify-content:center;align-items:flex-end;margin-bottom:10px}
.benefit-body h3{font-family:"Poppins",sans-serif;font-size:20px;font-weight:600;color:var(--maroon)}
.benefit-body p{font-size:12px;line-height:19px;color:#6b5f62;margin-top:10px}

.quote-box{left:116px;top:2817px;width:968px;height:204px;background:#fbf3ee}
.quote-box .inner{position:absolute;left:7px;top:7px;right:7px;bottom:7px;border:1.5px solid #d8b6a6}
.quote-mark{left:197px;top:2858px;font-family:"Poppins",sans-serif;font-size:110px;font-weight:800;line-height:1;color:var(--maroon)}
.quote-text{left:289px;top:2862px;width:740px;font-size:26px;line-height:35px;font-style:italic;color:var(--maroon-dark)}
.quote-author{left:280px;top:2945px;font-family:"Poppins",sans-serif;font-size:20px;font-weight:600;color:var(--maroon)}

/* testimonials */
.testi-title{left:0;width:1200px;top:3124px;text-align:center;font-family:"Poppins",sans-serif;font-size:34px;color:var(--ink)}
.testi-title b{font-weight:700;color:var(--maroon)}
.testi-card{top:3217px;width:286px;height:281px;background:#fff;border:1.5px solid #dde5ef;border-radius:6px;box-shadow:0 6px 18px rgba(40,60,100,.06);padding:26px 38px 0 44px}
.testi-card .qm{font-family:"Poppins",sans-serif;font-size:30px;color:#6a6f7c;line-height:1}
.testi-card p{font-size:11px;line-height:19px;color:#3a3438;margin-top:14px}
.testi-card .who{display:flex;align-items:center;gap:10px;margin-top:12px}
.avatar{width:32px;height:32px;border-radius:50%;background:linear-gradient(135deg,#c9b6ab,#7f6f69)}
.stars{color:#f0b429;font-size:10px;letter-spacing:1px}
.name{font-family:"Poppins",sans-serif;font-size:11px;font-weight:600;color:var(--ink)}
.edge-card{top:3207px;width:66px;height:300px;background:#fff;border:1.5px solid #e9edf2}
.arrow{top:3343px}

/* contact */
.contact{left:155px;top:3559px;width:892px;height:458px;background:linear-gradient(180deg,#eccdbb 0%,#e9c9b7 60%,#efd5c6 100%);border-radius:4px}
.contact-title{left:155px;width:892px;top:3613px;text-align:center;font-family:"Poppins",sans-serif;font-size:33px;color:#3a2a2e}
.contact-title b{font-weight:700;color:var(--maroon-dark)}
.field{background:#fff;height:44px;display:flex;align-items:center;gap:8px;padding-left:20px;font-family:"Poppins",sans-serif;font-size:12px;font-weight:500;color:#3a3438}
.field.msg{align-items:flex-start;padding-top:14px;height:92px}
.submit{left:531px;top:3920px;width:153px;height:37px;border-radius:19px;background:var(--maroon);color:#fff;font-family:"Poppins",sans-serif;font-size:13px;font-weight:500;display:flex;align-items:center;justify-content:center}

/* footer */
.foot-logo{left:158px;top:4068px;font-family:"Poppins",sans-serif;font-size:30px;color:#2b2024;font-weight:500}
.foot-about{left:158px;top:4120px;width:230px;font-size:11px;line-height:15px;color:#6c6265}
.foot-head{font-family:"Poppins",sans-serif;font-size:17px;font-weight:600;color:#2b2024;border-left:3px solid var(--maroon);padding-left:12px;line-height:18px}
.foot-links{left:427px;top:4118px;font-family:"Poppins",sans-serif;font-size:15px;line-height:30px;color:#2b2024}
.foot-contact{display:flex;gap:14px;align-items:center;font-family:"Poppins",sans-serif;font-size:13px;line-height:20px;color:#3a3438}
.ci{width:32px;height:32px;border-radius:50%;background:var(--maroon);display:flex;align-items:center;justify-content:center;flex:none}
.social{left:907px;top:4122px;display:flex;gap:30px}
.social span{width:26px;height:26px;border:2.5px solid #2b2024;border-radius:50%;display:block}
.foot-rule{left:0;top:4323px;width:1200px;height:1px;background:#ddd}
.copyright{left:0;width:1200px;top:4341px;text-align:center;font-size:12px;color:#3a3438}
</style>
</head>
<body>

<!-- HERO -->
<section class="abs hero" aria-label="Hero"></section>
<div class="abs hero-photo" role="img" aria-label="Photo of a consultant with glasses working with holographic data charts"></div>
<div class="abs nav-logo">Novara Consult</div>
<nav class="abs nav-links"><span class="active">Home</span><span>About Us</span><span>Services</span></nav>
<div class="abs nav-cta">Contact Us ›</div>
<div class="abs hero-kicker">Welcome to Novara Consult</div>
<h1 class="abs hero-title"><b>Innovative Solution</b><br><span>Consulting Service</span></h1>
<p class="abs hero-text">Lorem ipsum dolor sit amet consectetur adipiscing elit sed do eiusmod tempor incididunt ut</p>
<div class="abs hero-btn">Contact Us ›</div>
<svg class="abs scroll-badge" width="104" height="104" viewBox="0 0 104 104">
  <defs><path id="ring" d="M52,52 m-40,0 a40,40 0 1,1 80,0 a40,40 0 1,1 -80,0"/></defs>
  <text font-family="Montserrat,sans-serif" font-size="10" letter-spacing="2" fill="#3a2a2e"><textPath href="#ring">SCROLL DOWN · SCROLL DOWN ·</textPath></text>
  <circle cx="52" cy="52" r="20" fill="none" stroke="#3a2a2e" stroke-width="1.5"/>
  <path d="M52 42v18M45 54l7 7 7-7" fill="none" stroke="#3a2a2e" stroke-width="1.8"/>
</svg>
<svg class="abs" style="left:0;top:700px" width="1200" height="40" viewBox="0 0 1200 40">
  <path d="M0 16H520C560 16 560 4 600 4S640 30 680 16H1200" fill="none" stroke="#c9a9a0" stroke-width="1.5"/>
</svg>

<!-- PROBLEMS -->
<section class="abs problems" aria-label="Problems"></section>
<h2 class="abs sec-title" style="top:806px">Problems</h2>
<div class="abs photo-circle" role="img" aria-label="Photo of a stressed man at a laptop holding his head" style="left:92px;top:880px;width:452px;height:452px;background:radial-gradient(circle at 50% 40%,#e9e0cf 0%,#cdbfa6 45%,#8d7f6c 100%)"></div>
<svg class="abs" style="left:510px;top:940px" width="180" height="330" viewBox="0 0 180 330">
  <g fill="none" stroke="#d9d3b4" stroke-width="6">
    <path d="M0 165C60 165 80 165 110 110S150 15 172 15"/>
    <path d="M0 165H172"/>
    <path d="M0 165C60 165 80 165 110 220S150 315 172 315"/>
  </g>
  <g fill="none" stroke="#fff" stroke-width="1.5" stroke-dasharray="2 3">
    <path d="M0 165C60 165 80 165 110 110S150 15 172 15"/>
    <path d="M0 165H172"/>
    <path d="M0 165C60 165 80 165 110 220S150 315 172 315"/>
  </g>
</svg>

<div class="abs prob-card" style="top:900px">
  <div class="icon"><svg width="44" height="44" viewBox="0 0 44 44" fill="none" stroke="#fff" stroke-width="2"><circle cx="22" cy="22" r="14"/><circle cx="22" cy="22" r="5"/><path d="M22 4v6M22 34v6M4 22h6M34 22h6"/></svg></div>
  <div class="txt"><div class="card-h">Problem Heading</div><div class="card-p">Lorem ipsum dolor sit amet, consectetur adipiscing elit, sed do eiusmod tempor</div></div>
</div>
<div class="abs prob-card" style="top:1048px">
  <div class="icon"><svg width="44" height="44" viewBox="0 0 44 44" fill="none" stroke="#fff" stroke-width="2"><ellipse cx="22" cy="22" rx="17" ry="7"/><ellipse cx="22" cy="22" rx="17" ry="7" transform="rotate(60 22 22)"/><ellipse cx="22" cy="22" rx="17" ry="7" transform="rotate(-60 22 22)"/><circle cx="22" cy="22" r="2.5" fill="#fff"/></svg></div>
  <div class="txt"><div class="card-h">Problem Heading</div><div class="card-p">Lorem ipsum dolor sit amet, consectetur adipiscing elit, sed do eiusmod tempor</div></div>
</div>
<div class="abs prob-card" style="top:1202px">
  <div class="icon"><svg width="44" height="44" viewBox="0 0 44 44" fill="none" stroke="#fff" stroke-width="2"><rect x="8" y="8" width="28" height="22" rx="2"/><path d="M14 36h16M22 30v6M14 24l6-7 5 4 6-8"/></svg></div>
  <div class="txt"><div class="card-h">Problem Heading</div><div class="card-p">Lorem ipsum dolor sit amet, consectetur adipiscing elit, sed do eiusmod tempor</div></div>
</div>

<!-- SOLUTIONS -->
<section class="abs solutions" aria-label="Solutions"></section>
<h2 class="abs sec-title" style="top:1471px">Solutions</h2>
<div class="abs photo-circle" role="img" aria-label="Photo of a smiling businesswoman holding a laptop" style="left:650px;top:1536px;width:452px;height:452px;background:radial-gradient(circle at 50% 45%,#eef0f5 0%,#c9cde2 45%,#6c74a8 100%)"></div>
<svg class="abs" style="left:471px;top:1590px" width="220" height="330" viewBox="0 0 220 330">
  <g fill="none" stroke="#cfe6c4" stroke-width="6">
    <path d="M0 14C40 14 60 14 90 80S150 167 215 167"/>
    <path d="M0 162H215"/>
    <path d="M0 316C40 316 60 316 90 250S150 167 215 167"/>
  </g>
  <g fill="none" stroke="#7fc98b" stroke-width="1.5" stroke-dasharray="2 3">
    <path d="M0 14C40 14 60 14 90 80S150 167 215 167"/>
    <path d="M0 162H215"/>
    <path d="M0 316C40 316 60 316 90 250S150 167 215 167"/>
  </g>
</svg>

<div class="abs sol-card" style="top:1549px">
  <div class="txt"><div class="card-h">Solution Heading</div><div class="card-p">Lorem ipsum dolor sit amet, consectetur adipiscing eit sed do eiusm</div></div>
  <div class="icon"><svg width="44" height="44" viewBox="0 0 44 44" fill="none" stroke="#fff" stroke-width="2"><circle cx="20" cy="24" r="11"/><circle cx="20" cy="24" r="4"/><circle cx="33" cy="11" r="6"/></svg></div>
</div>
<div class="abs sol-card" style="top:1697px">
  <div class="txt"><div class="card-h">Solution Heading</div><div class="card-p">Lorem ipsum dolor sit amet, consectetur adipiscing eit sed do eiusm</div></div>
  <div class="icon"><svg width="44" height="44" viewBox="0 0 44 44" fill="none" stroke="#fff" stroke-width="2"><rect x="6" y="8" width="32" height="22" rx="2"/><path d="M14 36h16M22 30v6M12 24v-4M18 24v-8M24 24v-6M30 24v-10"/></svg></div>
</div>
<div class="abs sol-card" style="top:1852px">
  <div class="txt"><div class="card-h">Solution Heading</div><div class="card-p">Lorem ipsum dolor sit amet, consectetur adipiscing eit sed do eiusm</div></div>
  <div class="icon"><svg width="44" height="44" viewBox="0 0 44 44" fill="none" stroke="#fff" stroke-width="2"><path d="M8 36h28M12 36V24M19 36V18M26 36V22M33 36V12M10 18l9-8 7 6 9-9"/></svg></div>
</div>
<svg class="abs" style="left:0;top:2055px" width="1200" height="40" viewBox="0 0 1200 40">
  <path d="M0 20H540C570 20 580 6 600 6S630 34 660 20H1200" fill="none" stroke="#c9a9a0" stroke-width="1.5"/>
</svg>

<!-- BENEFITS -->
<section class="abs benefits" aria-label="Our Benefits"></section>
<h2 class="abs benefit-title">Our <b>Benefits</b></h2>

<div class="abs diamond" style="left:114px;top:2270px"></div>
<div class="abs diamond" style="left:478px;top:2270px"></div>
<div class="abs diamond" style="left:830px;top:2270px"></div>
<div class="abs diamond" style="left:294px;top:2469px"></div>
<div class="abs diamond" style="left:652px;top:2469px"></div>

<div class="abs benefit-body" style="left:115px;top:2290px">
  <div class="icon"><svg width="56" height="56" viewBox="0 0 56 56" fill="none" stroke="#5b1628" stroke-width="2"><path d="M20 30a10 10 0 1 1 16 0c-2 2-3 4-3 7h-10c0-3-1-5-3-7z"/><path d="M23 42h10M24 46h8M28 4v6M12 12l4 4M44 12l-4 4M6 26h6M44 26h6"/></svg></div>
  <h3>Benefit Heading</h3>
  <p>Lorem ipsum dolor sit amet, consectetur adipiscing elit, sed do eiusmod tempor incidi</p>
</div>
<div class="abs benefit-body" style="left:479px;top:2290px">
  <div class="icon"><svg width="56" height="56" viewBox="0 0 56 56" fill="none" stroke="#5b1628" stroke-width="2"><circle cx="28" cy="14" r="7"/><circle cx="12" cy="30" r="5"/><circle cx="44" cy="30" r="5"/><path d="M18 50c0-10 4-16 10-16s10 6 10 16M4 50c0-6 3-10 8-10M52 50c0-6-3-10-8-10"/></svg></div>
  <h3>Team Consulting</h3>
  <p>Lorem ipsum dolor sit amet, consectetur adipiscing elit, sed do eiusmod tempor incidi</p>
</div>
<div class="abs benefit-body" style="left:831px;top:2290px">
  <div class="icon"><svg width="56" height="56" viewBox="0 0 56 56" fill="none" stroke="#5b1628" stroke-width="2"><path d="M16 48v-8c-6-3-9-9-9-16a20 20 0 0 1 40 0l4 8h-5v8h-8v8"/><circle cx="26" cy="22" r="6"/></svg></div>
  <h3>Benefit Heading</h3>
  <p>Lorem ipsum dolor sit amet, consectetur adipiscing elit, sed do eiusmod tempor incidi</p>
</div>
<div class="abs benefit-body" style="left:295px;top:2488px">
  <div class="icon"><svg width="56" height="56" viewBox="0 0 56 56" fill="none" stroke="#5b1628" stroke-width="2"><rect x="6" y="6" width="44" height="44" rx="3"/><path d="M6 14h44"/><circle cx="28" cy="32" r="12"/><circle cx="28" cy="32" r="6"/><circle cx="28" cy="32" r="1.5" fill="#5b1628"/></svg></div>
  <h3>Optimization</h3>
  <p>Lorem ipsum dolor sit amet, consectetur adipiscing elit, sed do eiusmod tempor incidi</p>
</div>
<div class="abs benefit-body" style="left:653px;top:2488px">
  <div class="icon"><svg width="56" height="56" viewBox="0 0 56 56" fill="none" stroke="#5b1628" stroke-width="2"><circle cx="28" cy="28" r="22" stroke-dasharray="6 3"/><circle cx="28" cy="28" r="13"/><circle cx="28" cy="28" r="5"/></svg></div>
  <h3>Benefit Heading</h3>
  <p>Lorem ipsum dolor sit amet, consectetur adipiscing elit, sed do eiusmod tempor incidi</p>
</div>

<div class="abs quote-box"><div class="inner"></div></div>
<div class="abs quote-mark">“</div>
<p class="abs quote-text">We cannot solve our problems with the same thinking we used when we created them</p>
<div class="abs quote-author">- Marcus Hale</div>

<!-- TESTIMONIALS -->
<h2 class="abs testi-title">What Our Client <b>are Saying</b></h2>
<div class="abs edge-card" style="left:0"></div>
<div class="abs edge-card" style="left:1134px"></div>

<div class="abs testi-card" style="left:153px">
  <div class="qm">66</div>
  <p>"Lorem ipsum dolor sit amet, consectetur adipiscing elit, sed do eiusmod tempor incididunt ut labore et dolore magna aliqua. Ut enim ad minim veniam, quis nostrud exercitation ullamco laboris nisi ut aliquip ex ea commodo consequatoute</p>
  <div class="who"><div class="avatar"></div><div><div class="stars">★★★★★</div><div class="name">Daniel Reyes</div></div></div>
</div>
<div class="abs testi-card" style="left:455px">
  <div class="qm">66</div>
  <p>"Lorem ipsum dolor sit amet, consectetur adipiscing elit, sed do eiusmod tempor incididunt ut labore et dolore magna aliqua. Ut enim ad minim veniam, quis nostrud exercitation ullamco laboris nisi ut aliquip ex ea commodo consequatoute</p>
  <div class="who"><div class="avatar"></div><div><div class="stars">★★★★★</div><div class="name">Daniel Reyes</div></div></div>
</div>
<div class="abs testi-card" style="left:761px">
  <div class="qm">66</div>
  <p>"Lorem ipsum dolor sit amet, consectetur adipiscing elit, sed do eiusmod tempor incididunt ut labore et dolore magna aliqua. Ut enim ad minim veniam, quis nostrud exercitation ullamco laboris nisi ut aliquip ex ea commodo consequatoute</p>
  <div class="who"><div class="avatar"></div><div><div class="stars">★★★★★</div><div class="name">Daniel Reyes</div></div></div>
</div>
<svg class="abs arrow" style="left:94px" width="22" height="36" viewBox="0 0 22 36"><path d="M18 4L5 18l13 14" fill="none" stroke="#17203d" stroke-width="3.5"/></svg>
<svg class="abs arrow" style="left:1090px" width="22" height="36" viewBox="0 0 22 36"><path d="M4 4l13 14L4 32" fill="none" stroke="#17203d" stroke-width="3.5"/></svg>

<!-- CONTACT -->
<section class="abs contact" aria-label="Contact form"></section>
<h2 class="abs contact-title">Get <b>in Touch with Us</b></h2>
<div class="abs field" style="left:310px;top:3690px;width:296px"><svg width="12" height="12" viewBox="0 0 12 12" fill="#8a8a8a"><circle cx="6" cy="3.5" r="3"/><path d="M0 12c0-4 3-5 6-5s6 1 6 5z"/></svg>First Name*</div>
<div class="abs field" style="left:618px;top:3690px;width:298px"><svg width="12" height="12" viewBox="0 0 12 12" fill="#8a8a8a"><circle cx="6" cy="3.5" r="3"/><path d="M0 12c0-4 3-5 6-5s6 1 6 5z"/></svg>Last Name*</div>
<div class="abs field" style="left:310px;top:3743px;width:296px"><svg width="14" height="11" viewBox="0 0 14 11" fill="none" stroke="#8a8a8a" stroke-width="1.5"><rect x="1" y="1" width="12" height="9"/><path d="M1 1l6 5 6-5"/></svg>Email address*</div>
<div class="abs field" style="left:618px;top:3743px;width:298px"><svg width="12" height="12" viewBox="0 0 12 12" fill="#8a8a8a"><path d="M2 0l3 3-1.5 2a7 7 0 0 0 3.5 3.5L9 7l3 3-2 2C5 12 0 7 0 2z"/></svg>Phone*</div>
<div class="abs field msg" style="left:310px;top:3801px;width:606px"><svg width="13" height="12" viewBox="0 0 13 12" fill="#8a8a8a"><path d="M6.5 0C10 0 13 2 13 5s-3 5-6.5 5L3 12l1-3C1.5 8 0 7 0 5c0-3 3-5 6.5-5z"/></svg>Leave Message</div>
<div class="abs submit">Submit Now ›</div>

<!-- FOOTER -->
<div class="abs foot-logo">Novara Consult</div>
<p class="abs foot-about">Lorem ipsum dolor sit amet, consectetur adipiscing elit, sed do eiusmod tempor incididunt ut labore et dolore magna aliqua. Quis ipsum suspendisse ultrices gravida</p>
<div class="abs foot-head" style="left:414px;top:4075px">NAVGATION</div>
<div class="abs foot-links">Home<br>About us<br>Services<br>Contact us</div>
<div class="abs foot-head" style="left:630px;top:4077px">CONTACT US</div>
<div class="abs foot-contact" style="left:638px;top:4120px"><div class="ci"><svg width="14" height="11" viewBox="0 0 14 11" fill="none" stroke="#fff" stroke-width="1.5"><rect x="1" y="1" width="12" height="9"/><path d="M1 1l6 5 6-5"/></svg></div><div>Email us at<br>info@novaraconsult.com</div></div>
<div class="abs foot-contact" style="left:638px;top:4190px"><div class="ci"><svg width="13" height="13" viewBox="0 0 12 12" fill="#fff"><path d="M2 0l3 3-1.5 2a7 7 0 0 0 3.5 3.5L9 7l3 3-2 2C5 12 0 7 0 2z"/></svg></div><div>Phone Support<br>(555) 014 2290</div></div>
<div class="abs foot-head" style="left:899px;top:4075px">FOLLOW US</div>
<div class="abs social"><span aria-label="Social profile one"></span><span aria-label="Social profile two"></span><span aria-label="Social profile three"></span></div>
<div class="abs foot-rule"></div>
<div class="abs copyright">© 2025 Novara Consult. All Rights Reserved</div>

</body>
</html>
```